Consulting Company needs business card design

We need a business card design for a new consulting and business solutions company based in Bermuda called Corvale Partners Limited. Looking for a double sided business card with one side only including the company logo thats attached and the other including contact information. Logo contains blue and turquoise colors and is fine to be on both sides of the card.
Contact Information for Business Card
Corvale Partners Limited
P.O. Box HM318
Devonshire DV BX
Bermuda
Name: Marcus Pellegrin
Position: Director
Telephone: 1 441 733 4906
Email: mpellegrin@corvale.example
Website: www.corvale.example

```html
<!DOCTYPE html>
<html lang="en">
<head>
<meta charset="utf-8">
<title>Corvale Partners Limited — Business Card</title>
<link rel="stylesheet" href="https://fonts.googleapis.com/css2?family=Montserrat:wght@300;500&family=Arimo:wght@400;700&display=swap">
<style>
  :root {
    --stage: #2b2b2d;
    --card-blue: #29a8df;
    --brand-blue: #2592cf;
    --brand-teal: #1f9e9a;
    --paper: #ffffff;
    --ink: #1e1e1e;
    --white: #ffffff;
  }
  * { box-sizing: border-box; margin: 0; padding: 0; }
  html, body {
    width: 1200px; height: 997px; overflow: hidden;
    background: var(--stage);
  }
  .canvas { position: relative; width: 1200px; height: 997px; }

  .card {
    position: absolute; width: 600px; height: 343px;
    border-radius: 4px;
    box-shadow: 0 18px 40px rgba(0,0,0,.45);
  }

  /* Front side */
  .card--front {
    left: 130px; top: 110px;
    background: var(--card-blue);
    display: flex; flex-direction: column; align-items: center; justify-content: center;
    color: var(--white);
  }
  .front-mark {
    width: 96px; height: 96px; border-radius: 50%;
    background: var(--white); margin-bottom: 26px;
  }
  .front-name {
    font-family: "Montserrat", sans-serif; font-weight: 500;
    font-size: 34px; letter-spacing: 3px; text-transform: uppercase;
  }

  /* Back side */
  .card--back {
    left: 470px; top: 530px;
    background: var(--paper);
    overflow: hidden;
  }
  .back-name {
    position: absolute; left: 36px; top: 34px;
    font-family: "Montserrat", sans-serif; font-weight: 500;
    font-size: 17px; letter-spacing: 1.5px; text-transform: uppercase;
    color: var(--brand-blue);
  }
  .back-mark {
    position: absolute; right: 40px; top: 46px;
    width: 250px; height: 250px; border-radius: 50%;
    background: linear-gradient(135deg, var(--brand-blue), var(--brand-teal));
  }
  .contact {
    position: absolute; left: 36px; top: 124px;
    font-family: "Arimo", sans-serif; color: var(--ink);
  }
  .contact__name { font-size: 19px; color: var(--brand-blue); }
  .contact__role { font-size: 13px; margin: 3px 0 16px; }
  .contact__list { list-style: none; font-size: 14px; line-height: 1.25; }
  .contact__list li { display: flex; align-items: flex-start; gap: 9px; margin-bottom: 7px; }
  .icon { flex: none; width: 16px; height: 16px; margin-top: 1px; }
  .contact__web {
    margin-top: 6px; font-weight: 700; font-size: 16px;
    letter-spacing: 2px; color: var(--brand-blue); text-transform: uppercase;
  }
</style>
</head>
<body>
<main class="canvas">

  <section class="card card--front" aria-label="Card front">
    <div class="front-mark"></div>
    <p class="front-name">Corvale Partners Limited</p>
  </section>

  <section class="card card--back" aria-label="Card back">
    <p class="back-name">Corvale Partners Limited</p>
    <div class="back-mark"></div>

    <div class="contact">
      <p class="contact__name">Marcus Pellegrin</p>
      <p class="contact__role">Director</p>
      <ul class="contact__list">
        <li>
          <svg class="icon" viewBox="0 0 16 16" aria-hidden="true">
            <circle cx="8" cy="8" r="8" fill="#2592cf"/>
            <path d="M5 4.5l1.6-.4.9 2-1 .8a5 5 0 0 0 2.6 2.6l.8-1 2 .9-.4 1.6c-3.6.3-6.8-2.9-6.5-6.5z" fill="#fff"/>
          </svg>
          1 441 733 4906
        </li>
        <li>
          <svg class="icon" viewBox="0 0 16 16" aria-hidden="true">
            <circle cx="8" cy="8" r="8" fill="#2592cf"/>
            <rect x="4" y="5" width="8" height="6" rx="1" fill="#fff"/>
            <path d="M4.3 5.4L8 8.3l3.7-2.9" stroke="#2592cf" stroke-width="1" fill="none"/>
          </svg>
          mpellegrin@corvale.example
        </li>
        <li>
          <svg class="icon" viewBox="0 0 16 16" aria-hidden="true">
            <circle cx="8" cy="8" r="8" fill="#2592cf"/>
            <path d="M8 3.5a3 3 0 0 0-3 3c0 2.3 3 5.8 3 5.8s3-3.5 3-5.8a3 3 0 0 0-3-3z" fill="#fff"/>
            <circle cx="8" cy="6.5" r="1.1" fill="#2592cf"/>
          </svg>
          <span>P.O. Box HM318, Devonshire<br>DV BX, Bermuda</span>
        </li>
      </ul>
      <p class="contact__web">www.corvale.example</p>
    </div>
  </section>

</main>
</body>
</html>
```